Filmproduktion braucht Visitenkarten und Briefpapier
Zielgruppe
Wir sind eine junge Filmproduktion Firma mit dem Namen Lichtkante.
Unser Kerngeschäft sind Image und Unternehmensfilme, sowie Event und Messefilme.
Aufgabenstellung
Wir sind junge, kreative, Filmschaffende und das soll sich auch in der Visitenkarte widerspiegeln, dennoch macht bitte auch ein paar klassische Vorschläge, manchmal ist weniger mehr.
Unser altes Briefpapier ist angehängt. Das neue Briefpapier muss von uns veränderbar sein, da wir noch nicht alle Daten haben wie Steuernummer und USt-ID, bitte aber schon als Dummy anlegen.
Unsere alten Visitenkarten sind angehängt, diese Daten Stimmen, aber ansonsten stimmt daran nix, wie wir finden. Bitte nicht daran Orientieren!!!
Bitte bei der Adresse Lichtkante GbR schreiben.
Unser neues Logo, jetzt in blau ist ebenfalls angehängt.
Viel Spass beim Designen.

```html
<!DOCTYPE html>
<html lang="de">
<head>
<meta charset="utf-8">
<title>Lichtkante – Briefpapier</title>
<link rel="stylesheet" href="https://fonts.googleapis.com/css2?family=Source+Sans+3:wght@400;600&display=swap">
<style>
  :root{
    --brand-blue:#4a93d2;
    --brand-blue-light:#8dbde6;
    --ink:#2b2b2b;
    --muted:#666;
    --rule:#8a8a8a;
    --paper:#ffffff;
    --sig-tint:#f1f4f8;
  }
  *{margin:0;padding:0;box-sizing:border-box}
  html,body{width:849px;height:1200px;overflow:hidden;background:var(--paper)}
  body{font-family:"Source Sans 3",sans-serif;color:var(--ink);position:relative}
  .sheet{position:relative;width:849px;height:1200px;overflow:hidden}
  .band-top{position:absolute;left:0;top:0;width:849px;height:21px;background:var(--brand-blue)}
  .band-top-tab{position:absolute;left:639px;top:20px;width:210px;height:21px;background:var(--brand-blue)}
  .band-bottom{position:absolute;left:0;top:1186px;width:849px;height:14px;background:var(--brand-blue)}
  .header-url{position:absolute;left:639px;top:46px;font-size:16px;color:var(--brand-blue);white-space:nowrap}
  .brand-name{position:absolute;left:120px;top:170px;font-size:20px;font-weight:600;letter-spacing:12px;color:var(--ink);text-transform:uppercase;display:flex;align-items:center;white-space:nowrap}
  .brand-dot{width:12px;height:12px;border-radius:50%;background:var(--ink);margin-right:14px}
  .subject{position:absolute;left:122px;top:219px;font-size:22px;line-height:24px}
  .subject-kicker{color:var(--brand-blue)}
  .subject-title{color:var(--ink);text-transform:uppercase}
  .date-bar{position:absolute;left:106px;top:274px;width:198px;height:22px;
    background:linear-gradient(90deg,var(--brand-blue) 0,var(--brand-blue) 78%,var(--brand-blue-light) 100%);
    color:#fff;font-size:13.5px;line-height:22px;padding-left:16px}
  .letter-body{position:absolute;left:122px;top:321px;width:650px;font-size:13.6px;line-height:28.5px;color:var(--ink)}
  .letter-body p{margin-bottom:28.5px}
  .signature-area{position:absolute;left:122px;top:928px;width:144px;height:46px;background:var(--sig-tint);border-radius:4px}
  .signature-rule{position:absolute;left:100px;top:977px;width:202px;height:1px;background:var(--rule)}
  .signer-role{position:absolute;left:122px;top:983px;font-size:10.5px;line-height:14px;color:var(--brand-blue)}
  .signer-company{position:absolute;left:122px;top:998px;font-size:9.5px;line-height:13px;color:var(--muted)}
  .contact-icon{position:absolute;top:1116px;width:29px;height:29px;background:linear-gradient(180deg,#6aaae0,var(--brand-blue));display:flex;align-items:center;justify-content:center}
  .contact-lines{position:absolute;top:1111px;font-size:10.5px;line-height:18px;color:var(--muted);white-space:nowrap}
  .icon-web{left:122px}
  .lines-web{left:162px}
  .icon-phone{left:291px}
  .lines-phone{left:332px}
  .icon-address{left:453px}
  .lines-address{left:494px}
  .tax-ids{position:absolute;left:122px;top:1160px;font-size:9px;line-height:12px;color:var(--muted);white-space:nowrap}
</style>
</head>
<body>
<div class="sheet">
  <div class="band-top"></div>
  <div class="band-top-tab"></div>
  <div class="header-url">www.lichtkante.example</div>

  <div class="brand-name"><span class="brand-dot"></span>Lichtkante</div>

  <div class="subject">
    <div class="subject-kicker">Lorem</div>
    <div class="subject-title">Ipsum Dolor</div>
  </div>
  <div class="date-bar">15.10.2013</div>

  <div class="letter-body">
    <p>Sit amet, consectetur adipiscing elit. Quisque fringilla quam quis odio auctor in egestas ante pharetra. Fusce placerat tempor turpis vel euismod. Donec metus diam, interdum nec gravida tincidunt, molestie sit amet nisl. Aliquam pharetra tempus lorem, vitae ullamcorper magna scelerisque sit amet. Quisque et porttitor dolor. Ut dapibus, turpis quis lacinia cursus, risus ante cursus risus, vel luctus erat magna a ligula. Phasellus vulputate sapien orci, sed bibendum nisl. Cras dignissim, sapien ac cursus commodo, elit magna vulputate tellus, id sagittis enim dolor nec felis. Aliquam ornare lorem ut ipsum ullamcorper commodo. Curabitur tristique rutrum erat, iaculis laoreet libero sagittis non.</p>
    <p>Sed quis diam felis. Ut a sapien vitae eros feugiat feugiat. Vivamus pulvinar commodo cursus. Etiam vulputate vulputate justo, et fermentum orci convallis non. Maecenas elit odio, gravida in congue et, porta sed ipsum. Morbi quis ligula nec nulla posuere lobortis vel et dolor. Ut neque dui, sollicitudin id gravida ut, fermentum ac nibh.</p>
    <p>Mauris rutrum velit tincidunt dolor tristique ac adipiscing odio auctor. Cras leo magna, ultrices volutpat egestas ut, pellentesque eget purus. Fusce fringilla, metus et congue eleifend, ligula eros viverra nibh, sit amet placerat eros justo sed libero. Ut feugiat ligula sed nisi condimentum tempus. Ut eu libero purus, luctus blandit felis. Phasellus in diam ipsum, vitae tempus odio. Nullam pellentesque mauris in ligula consectetur.</p>
    <p>Suspendisse elementum dictum leo et rutrum. Duis faucibus dolor sit amet justo tincidunt fermentum. Duis nisi velit, ultricies vitae rutrum eget, convallis at lectus.</p>
  </div>

  <div class="signature-area" role="img" aria-label="Handschriftliche Unterschrift der Geschäftsführung"></div>
  <div class="signature-rule"></div>
  <div class="signer-role">GESCHÄFTSFÜHRER</div>
  <div class="signer-company">LICHTKANTE GbR</div>

  <div class="contact-icon icon-web">
    <svg width="17" height="17" viewBox="0 0 20 20" fill="none" stroke="#fff" stroke-width="1.5">
      <circle cx="10" cy="10" r="8"/><ellipse cx="10" cy="10" rx="3.5" ry="8"/>
      <line x1="2" y1="10" x2="18" y2="10"/><line x1="3.5" y1="6" x2="16.5" y2="6"/><line x1="3.5" y1="14" x2="16.5" y2="14"/>
    </svg>
  </div>
  <div class="contact-lines lines-web">www.lichtkante.example<br>post@lichtkante.example</div>

  <div class="contact-icon icon-phone">
    <svg width="12" height="19" viewBox="0 0 12 20" fill="#fff">
      <rect x="3" y="0" width="1.6" height="4"/>
      <rect x="1" y="3.5" width="10" height="16" rx="1.5"/>
      <rect x="3" y="6" width="6" height="4" fill="#4a93d2"/>
      <rect x="3" y="12" width="6" height="5" fill="#4a93d2" opacity=".5"/>
    </svg>
  </div>
  <div class="contact-lines lines-phone">0301234567<br>0176543210</div>

  <div class="contact-icon icon-address">
    <svg width="18" height="16" viewBox="0 0 20 18" fill="#fff">
      <polygon points="10,0 20,9 17,9 17,18 12,18 12,12 8,12 8,18 3,18 3,9 0,9"/>
    </svg>
  </div>
  <div class="contact-lines lines-address">Lindenweg 12<br>10115 Berlin</div>

  <div class="tax-ids">Steuernummer: 00/000/00000 &nbsp;·&nbsp; USt-IdNr.: DE000000000</div>

  <div class="band-bottom"></div>
</div>
</body>
</html>
```